Packaging Design Project

I am looking for an attractive Package (Background and Font) for my upcoming item I will be Importing. I am open to different types of Design, however, I want it to look Professional. I will upload a couple of Files. One will be my Logo, which is called Pantaro. The other file, will be a Skull which I want incorporated on the Package if possible. I will also upload an example of a package. However, I dont like the way this is designed and the Font is too plain.

```html
<!DOCTYPE html>
<html lang="en">
<head>
<meta charset="UTF-8">
<title>Pantaro Packaging – PX-15.4FD</title>
<link rel="stylesheet" href="https://fonts.googleapis.com/css2?family=Orbitron:wght@500;700;800&display=swap">
<style>
  :root {
    --page-bg: #ebebeb;
    --panel-black: #161616;
    --panel-charcoal: #242424;
    --brand-red: #d8201f;
    --deep-red: #8e0f10;
    --stripe-red: #b3191a;
    --text-white: #f2f2f2;
    --glass-grey: #8a8a8a;
  }
  html, body {
    margin: 0;
    width: 1200px;
    height: 848px;
    overflow: hidden;
    background: var(--page-bg);
  }
  .package-face {
    position: absolute;
    left: 110px;
    top: 32px;
    width: 980px;
    height: 783px;
    overflow: hidden;
    background:
      radial-gradient(ellipse at 60% 100%, rgba(142,15,16,0.75) 0%, rgba(142,15,16,0) 45%),
      radial-gradient(ellipse at 10% 95%, rgba(142,15,16,0.6) 0%, rgba(142,15,16,0) 35%),
      linear-gradient(160deg, var(--panel-charcoal), var(--panel-black));
  }
  .red-band {
    position: absolute;
    left: 227px;
    top: 0;
    width: 205px;
    height: 100%;
  }
  .glass-art {
    position: absolute;
    left: 432px;
    top: 0;
    width: 548px;
    height: 160px;
    background: linear-gradient(200deg, rgba(138,138,138,0.75), rgba(60,60,60,0.25) 60%, rgba(22,22,22,0));
  }
  .skull-art {
    position: absolute;
    left: 52px;
    top: 256px;
    width: 490px;
    height: 430px;
    background: radial-gradient(ellipse at 50% 48%, #ffffff 0%, #e6e6e6 30%, rgba(216,32,31,0.7) 52%, rgba(22,22,22,0) 72%);
  }
  .brand-name {
    position: absolute;
    left: 97px;
    top: 124px;
    margin: 0;
    font-family: "Orbitron", sans-serif;
    font-weight: 800;
    font-size: 80px;
    line-height: 90px;
    letter-spacing: 3px;
    color: var(--text-white);
  }
  .model-code {
    position: absolute;
    left: 611px;
    top: 296px;
    margin: 0;
    font-family: "Orbitron", sans-serif;
    font-weight: 700;
    font-size: 48px;
    line-height: 56px;
    letter-spacing: 3px;
    color: var(--brand-red);
  }
  .feature-rule {
    position: absolute;
    left: 652px;
    top: 331px;
    width: 6px;
    height: 251px;
    background: var(--brand-red);
  }
  .feature-list {
    position: absolute;
    left: 681px;
    top: 376px;
    margin: 0;
    padding: 0;
    list-style: none;
    font-family: "Orbitron", sans-serif;
    font-weight: 500;
    font-size: 12.5px;
    line-height: 21.4px;
    letter-spacing: 1.6px;
    text-transform: uppercase;
    color: var(--text-white);
  }
  .feature-list .feature-heading {
    color: var(--brand-red);
    font-weight: 700;
  }
</style>
</head>
<body>
  <main class="package-face">
    <svg class="red-band" viewBox="0 0 205 783" preserveAspectRatio="none" aria-hidden="true">
      <defs>
        <linearGradient id="bandFade" x1="0" y1="0" x2="0" y2="1">
          <stop offset="0" stop-color="#b3191a"/>
          <stop offset="0.7" stop-color="#9a1415"/>
          <stop offset="1" stop-color="#6e0c0d"/>
        </linearGradient>
      </defs>
      <rect width="205" height="783" fill="url(#bandFade)"/>
      <g fill="#161616">
        <polygon points="30,0 60,0 205,80 205,102"/>
        <polygon points="30,42 30,70 205,168 205,140"/>
        <polygon points="30,100 30,128 205,226 205,198"/>
        <polygon points="30,158 30,186 205,284 205,256"/>
      </g>
    </svg>

    <div class="glass-art" role="img" aria-label="Shattered glass and crystal spine illustration"></div>
    <div class="skull-art" role="img" aria-label="Skull and crossbones illustration with red light bursts"></div>

    <h1 class="brand-name">Pantaro</h1>

    <h2 class="model-code">PX-15.4FD</h2>
    <div class="feature-rule"></div>
    <ul class="feature-list">
      <li class="feature-heading">Features:</li>
      <li>TFT LCD Flipdown Monitor</li>
      <li>Super Slim Design</li>
      <li>On Screen Display Menu</li>
      <li>Display Mode: 16:9</li>
      <li>Swivel Screen</li>
      <li>High Resolution: 1024x768</li>
      <li>PAL/NTSC System</li>
      <li>Built-in IR Transmitter</li>
      <li>Dual Dome-Light</li>
    </ul>
  </main>
</body>
</html>
```